Membership Card Design

I need a basic membership card...it will entitle the customer to free entry to forthcoming promotions.
The business is called STARLANE PLAY and is a amusement arcade located in N Ireland.
I require .....
STARLANE PLAY MEMBER...across top of card in logo format.
Next line....this card entitles the holder free entry to forthcoming STARLANE EVENTS....
Then next line....customer name( space to write their name )
Next line.....customer mobile number ( space to write number )
On rear of card....logo/picture & STARLANE PLAY MEMBER written on back.

Industry/Entity Type

Business

Contact Information for Business Card

STARLANE PLAY
MEMBERSHIP CARD

```html
<!DOCTYPE html>
<html lang="en">
<head>
<meta charset="utf-8">
<title>Starlane Play Membership Card</title>
<link rel="stylesheet" href="https://fonts.googleapis.com/css2?family=Cinzel:wght@500;600&family=Open+Sans:wght@400;600;700&display=swap">
<style>
  :root {
    --page: #e9e7e4;
    --card-black: #050505;
    --card-charcoal: #2a2a2a;
    --silver-light: #f2f2f2;
    --silver-mid: #b9b9b9;
    --silver-dark: #6e6e6e;
    --text-white: #ffffff;
    --rule: #8a8a8a;
    --photo-teal: #1d4a52;
    --photo-red: #5a1424;
  }
  * { box-sizing: border-box; margin: 0; padding: 0; }
  html, body {
    width: 1200px;
    height: 1000px;
    overflow: hidden;
    background: var(--page);
  }
  .sheet {
    position: relative;
    width: 1200px;
    height: 1000px;
  }
  .card {
    position: absolute;
    left: 250px;
    width: 700px;
    height: 420px;
    border-radius: 28px;
    overflow: hidden;
    box-shadow: 0 10px 28px rgba(0,0,0,0.25);
  }
  .card--front { top: 50px; }
  .card--back {
    top: 530px;
    background: radial-gradient(ellipse at 50% 25%, var(--card-charcoal) 0%, #111 55%, var(--card-black) 100%);
    color: var(--text-white);
    text-align: center;
    font-family: "Open Sans", sans-serif;
  }
  .card--front svg { display: block; }
  .brand-name {
    font-family: "Cinzel", serif;
    font-weight: 600;
    fill: var(--silver-light);
  }
  .band-label {
    font-family: "Cinzel", serif;
    font-weight: 600;
    font-size: 30px;
    fill: var(--text-white);
    letter-spacing: 1px;
  }
  .back-title {
    margin-top: 38px;
    font-family: "Cinzel", serif;
    font-weight: 500;
    font-size: 66px;
    line-height: 1;
    color: var(--silver-mid);
    letter-spacing: 2px;
  }
  .back-subtitle {
    margin-top: 6px;
    font-family: "Cinzel", serif;
    font-weight: 500;
    font-size: 34px;
    color: var(--silver-dark);
    letter-spacing: 3px;
  }
  .entitlement {
    margin-top: 26px;
    font-size: 21px;
    line-height: 1.3;
  }
  .entitlement strong {
    display: block;
    font-weight: 700;
    font-size: 20px;
  }
  .fields {
    margin: 28px 60px 0 90px;
    text-align: left;
  }
  .field {
    display: flex;
    align-items: flex-end;
    gap: 10px;
    font-weight: 600;
    font-size: 24px;
    margin-bottom: 16px;
  }
  .field-line {
    flex: 1;
    border-bottom: 2px solid var(--rule);
    margin-bottom: 7px;
  }
</style>
</head>
<body>
<main class="sheet">
  <section class="card card--front">
    <svg width="700" height="420" viewBox="0 0 700 420" xmlns="http://www.w3.org/2000/svg">
      <defs>
        <radialGradient id="photo-tone" cx="50%" cy="55%" r="60%">
          <stop offset="0%" stop-color="var(--photo-teal)"/>
          <stop offset="45%" stop-color="#1a1a22"/>
          <stop offset="75%" stop-color="var(--photo-red)" stop-opacity="0.35"/>
          <stop offset="100%" stop-color="var(--card-black)"/>
        </radialGradient>
        <linearGradient id="silver-band" x1="0" y1="0" x2="1" y2="0">
          <stop offset="0%" stop-color="var(--silver-dark)"/>
          <stop offset="35%" stop-color="var(--silver-light)"/>
          <stop offset="70%" stop-color="var(--silver-mid)"/>
          <stop offset="100%" stop-color="var(--silver-dark)"/>
        </linearGradient>
        <path id="band-curve" d="M-10,420 Q330,330 710,250"/>
      </defs>
      <rect class="card-base" width="700" height="420" fill="var(--card-black)"/>
      <rect class="arcade-photo" role="img" aria-label="Arcade gaming machines glowing in a dim room" x="110" y="40" width="480" height="320" fill="url(#photo-tone)"/>
      <text class="brand-name" x="350" y="118" font-size="50" text-anchor="middle">STARLANE PLAY</text>
      <path class="silver-band" d="M-10,420 Q330,330 710,250" fill="none" stroke="url(#silver-band)" stroke-width="52"/>
      <path class="band-fill-below" d="M-10,446 Q330,356 710,276 L710,430 L-10,430 Z" fill="#1c1c1c"/>
      <text class="band-label" dy="11">
        <textPath href="#band-curve" startOffset="50%" text-anchor="middle">STARLANE PLAY MEMBER</textPath>
      </text>
    </svg>
  </section>

  <section class="card card--back">
    <h1 class="back-title">STARLANE PLAY</h1>
    <p class="back-subtitle">MEMBER</p>
    <p class="entitlement">This card entitles the holder free entry to forthcoming
      <strong>STARLANE EVENTS</strong></p>
    <div class="fields">
      <div class="field"><span class="field-label">Customer name :</span><span class="field-line"></span></div>
      <div class="field"><span class="field-label">Customer mobile number :</span><span class="field-line"></span></div>
    </div>
  </section>
</main>
</body>
</html>
```